Real Estate Business Cards

Looking for a clean, sharp and professional look for our Real Estate investment Fund that invests in Multi Family Apartment buildings.

Target Market(s)

Real Estate Fund

Industry/Entity Type

Real Estate

Contact Information for Business Card

Company Description: Real Estate Investment Fund
Company Name: KRV Holdings
Name: Marcus Tovell
Cell: (917) 482-0957
Email: marcus@krvholdings-example.com
Website: www.krvholdings-example.com
Address: 148, 7th Street, Brooklyn NY 11217

Colors

Designer to choose colors to be used in the design.

Requirements
Nice to have
• Colors to match logo

```html
<!DOCTYPE html>
<html lang="en">
<head>
<meta charset="utf-8">
<title>KRV Holdings – Business Card</title>
<link href="https://fonts.googleapis.com/css2?family=Cormorant+Garamond:wght@500&family=Open+Sans:wght@400;700&display=swap" rel="stylesheet">
<style>
  :root {
    --backdrop: #9a9a9a;
    --brand-blue: #0d73ad;
    --card-white: #ffffff;
    --text-grey: #555a5f;
    --rule-blue: #1b78b3;
  }
  * { margin: 0; padding: 0; box-sizing: border-box; }
  html, body {
    width: 1133px; height: 1200px; overflow: hidden;
    background: var(--backdrop);
  }
  .stage { position: relative; width: 1133px; height: 1200px; }

  .card {
    position: absolute; left: 219px; width: 694px; height: 396px;
  }
  .card--front { top: 153px; background: var(--brand-blue); }
  .card--back { top: 649px; background: var(--card-white); }

  .wordmark {
    position: absolute; white-space: nowrap;
    font-family: "Cormorant Garamond", Georgia, serif;
    font-weight: 500; letter-spacing: 1px; line-height: 1;
  }
  .card--front .wordmark {
    right: 42px; top: 305px; font-size: 46px; color: var(--card-white);
  }
  .card--back .wordmark {
    left: 54px; top: 240px; font-size: 36px; color: var(--brand-blue);
  }
  .wordmark-square {
    position: absolute; left: 144px; top: 150px;
    width: 44px; height: 44px; background: var(--brand-blue);
  }

  .divider {
    position: absolute; left: 359px; top: 106px;
    width: 2px; height: 186px; background: var(--rule-blue);
  }

  .contact {
    position: absolute; left: 382px; top: 100px;
    font-family: "Open Sans", Arial, sans-serif; color: var(--text-grey);
    font-size: 19px; line-height: 25px;
  }
  .contact-name {
    font-weight: 700; color: var(--brand-blue);
    font-size: 26px; line-height: 32px; margin-bottom: 14px;
  }
  .contact-address { margin-bottom: 20px; }
  .contact-line { display: flex; align-items: center; gap: 5px; }
  .contact-line svg { width: 15px; height: 15px; flex: none; fill: var(--brand-blue); }
</style>
</head>
<body>
<main class="stage">
  <section class="card card--front">
    <div class="wordmark">KRV HOLDINGS</div>
  </section>

  <section class="card card--back">
    <div class="wordmark-square" aria-hidden="true"></div>
    <div class="wordmark">KRV HOLDINGS</div>
    <div class="divider"></div>
    <div class="contact">
      <div class="contact-name">MARCUS TOVELL</div>
      <div class="contact-address">148, 7th Street<br>Brooklyn NY 11217</div>
      <div class="contact-line">
        <svg viewBox="0 0 16 16" aria-hidden="true"><path d="M3.5 1.5l2.5 0 1 3.5-1.8 1.2a8 8 0 0 0 4.6 4.6L11 9l3.5 1v2.5c0 1-1 2-2 2A11 11 0 0 1 1.5 3.5c0-1 1-2 2-2z"/></svg>
        <span>(917) 482-0957</span>
      </div>
      <div class="contact-line">
        <svg viewBox="0 0 16 16" aria-hidden="true"><path d="M1.5 4h13v1.2L8 9 1.5 5.2z M1.5 6.6L8 10.4l6.5-3.8V12h-13z"/></svg>
        <span>marcus@krvholdings-example.com</span>
      </div>
      <div class="contact-line">
        <svg viewBox="0 0 16 16" aria-hidden="true"><circle cx="8" cy="8" r="6.5"/></svg>
        <span>www.krvholdings-example.com</span>
      </div>
    </div>
  </section>
</main>
</body>
</html>
```